velmorino.eu :: Design ideas (no coding) for key pages of Personalized greeting cards online store

We need your vision on modern, clean, easy to read user interface (UI) for online service of personalized printed products, like greeting cards, postcards, fridge magnets, clips and etc.
Your vision should include UI presentation for:
- Home page with login (including soc nets)
- Product Designer page
- Cart pages (products and address selection)
- Example of general internal page (pricing, terms, etc)
- Artist info and portfolio page
We are looking for ideas we will love, NOT complete design of a whole site.
Top design/vision will we used as a basement for separate contract on complete design of the site.

UI should be based on existing functionality with some extent. It should not break ideas or methods used on prototype but designers are free to offer own product presentations, designer’s layout and cart views.

Prototype:
English: http://velmorino.eu
Russian: http://velmorino.ru
Lithuanian: http://velmorino.lt

Target Market(s)

People of 16-45 y.o. who likes to be distinctive, personal.

Industry/Entity Type

Store

Requirements
Must have
• Your work should meet attached requirements.
Site is multilingual. Wording should assume varieties in length on different languages.
Clean and easy to read UI
Flat design preferrably
Should be based on assets which are free or available for royalty-free licensing
Should not have
• heavy, meaningless 3D and shadow effects
Show NOT copy sites like: plonkra.com, tarnwick.co.uk

```html
<!DOCTYPE html>
<html lang="en">
<head>
<meta charset="utf-8">
<title>Velmorino — Greeting Cards</title>
<link href="https://fonts.googleapis.com/css2?family=Roboto:wght@400;500;700&family=Open+Sans:wght@400;600&display=swap" rel="stylesheet">
<style>
:root{
  --navy:#2f4a68;
  --btn-blue:#4d80a8;
  --btn-blue-dark:#3a6790;
  --brand-red:#b5302c;
  --coral:#f0604e;
  --ink:#222;
  --line:#d9d9d9;
  --footer-bg:#efefef;
  --footer-text:#666;
  --cart:#2b2b2b;
}
*{box-sizing:border-box;margin:0;padding:0}
html,body{width:1138px;height:1200px;overflow:hidden;background:#fff}
body{position:relative;font-family:"Roboto",Arial,sans-serif;color:var(--ink)}
.topline{position:absolute;left:0;top:0;width:100%;height:5px;background:var(--navy)}
.util-btn{position:absolute;top:5px;height:22px;color:#fff;font-size:11px;display:flex;align-items:center;justify-content:center;gap:5px}
.util-btn.contacts{left:757px;width:73px;background:var(--btn-blue)}
.util-btn.login{left:833px;width:107px;background:var(--btn-blue-dark)}
.brand{position:absolute;left:186px;top:24px;width:76px;text-align:center}
.brand-square{width:54px;height:48px;margin:0 auto 6px;background:var(--brand-red)}
.brand-name{font-size:15px;color:var(--brand-red);font-weight:400}
.nav-media{position:absolute;top:24px;display:flex;flex-direction:column;align-items:center;font-size:12px;color:#333}
.nav-media svg{height:44px;margin-bottom:9px}
.nav-media .caret{position:absolute;right:-16px;bottom:3px;border:5px solid transparent;border-top:5px solid #222}
.nav-text{position:absolute;top:70px;font-size:12px;color:#333}
.cart{position:absolute;left:863px;top:61px;width:77px;height:27px;background:var(--cart);color:#fff;font-size:11px;font-weight:700;display:flex;align-items:center;padding-left:9px;gap:12px;border-radius:2px}
.colour-band{position:absolute;left:0;top:101px;width:100%;height:31px;background:var(--coral)}
.swatch{position:absolute;top:8px;width:15px;height:15px;border-radius:50%;border:1.5px solid #fff}
.hero{position:absolute;left:0;top:132px;width:100%;height:178px;background:linear-gradient(90deg,#c6a7a4,#b44a4c 20%,#d9cbb9 40%,#a7364a 60%,#cfd0c6 80%,#b85a5e)}
.tags{position:absolute;left:0;width:100%;display:flex;justify-content:center;gap:7px}
.tag{border:1.5px solid #fff;border-radius:4px;color:#fff;font-size:11px;padding:2px 9px;background:rgba(0,0,0,.35)}
.board{position:absolute;left:289px;top:221px;width:560px;height:720px;background:#fff}
.col{position:absolute;top:9px;width:175px;display:flex;flex-direction:column;gap:9px}
.card{background:#fff;border:1px solid var(--line);border-radius:3px;box-shadow:0 1px 2px rgba(0,0,0,.12);overflow:hidden}
.card-photo{width:100%}
.card-meta{display:flex;justify-content:space-between;align-items:center;padding:0 11px;height:28px;font-size:10px;border-bottom:1px solid #e6e6e6}
.card-price{font-size:12px;font-weight:500}
.card-pin{padding:7px 11px 9px;font-size:10px;line-height:1.15;color:#333}
.card-pin b{display:block;font-weight:500;margin-bottom:5px}
.spinner{position:absolute;left:552px;top:919px}
.footer{position:absolute;left:0;top:976px;width:100%;height:224px;background:var(--footer-bg);font-family:"Open Sans",Arial,sans-serif}
.f-col{position:absolute;top:25px}
.f-col h4{font-size:12px;font-weight:600;color:#333;margin-bottom:12px;letter-spacing:.2px}
.f-col li{list-style:none;font-size:10px;color:var(--footer-text);height:20px;padding-left:11px;position:relative;white-space:nowrap}
.f-col li::before{content:"";position:absolute;left:1px;top:4px;border:3px solid transparent;border-left:4px solid #999}
.pay{display:flex;gap:4px}
.pay span{height:22px;display:flex;align-items:center;justify-content:center;font-size:7px;font-weight:600;border:1px solid #333;color:#333;background:#fff;white-space:nowrap;overflow:hidden}
.copyright{position:absolute;left:816px;width:110px;top:164px;text-align:center;font-size:11px;color:#333;line-height:17px;white-space:nowrap}
</style>
</head>
<body>
<div class="topline"></div>
<div class="util-btn contacts">Contacts</div>
<div class="util-btn login"><svg width="9" height="10" viewBox="0 0 9 10"><rect x="1" y="4" width="7" height="6" fill="#fff"/><path d="M2.5 4V2.8a2 2 0 0 1 4 0V4" stroke="#fff" fill="none"/></svg>Member Login</div>

<div class="brand"><div class="brand-square"></div><div class="brand-name">Velmorino</div></div>

<div class="nav-media" style="left:290px"><svg viewBox="0 0 30 30" width="44"><g stroke="#b5302c" stroke-width="3.5" stroke-linecap="round"><line x1="15" y1="3" x2="15" y2="27"/><line x1="4" y1="9" x2="26" y2="21"/><line x1="4" y1="21" x2="26" y2="9"/></g></svg>All Medias</div>
<div class="nav-media" style="left:361px"><svg viewBox="0 0 60 40" width="66"><g fill="none" stroke="#b5302c" stroke-width="1.3"><path d="M8 2 L26 8 V38 L8 32Z"/><path d="M26 8 L52 16 L50 38 L26 38"/></g></svg>Greeting Cards<span class="caret"></span></div>
<div class="nav-media" style="left:466px"><svg viewBox="0 0 34 40" width="37"><g fill="none" stroke="#b5302c" stroke-width="1.3"><path d="M4 4 L16 2 V36 L4 38Z"/><path d="M16 2 L30 4 V38 L16 36"/></g></svg>Square Cards</div>
<div class="nav-media" style="left:560px"><svg viewBox="0 0 60 40" width="64"><g fill="none" stroke="#b5302c" stroke-width="1.3"><rect x="2" y="2" width="22" height="30"/><rect x="24" y="10" width="32" height="22"/></g></svg>Post Cards<span class="caret"></span></div>

<div class="nav-text" style="left:732px">Products</div>
<div class="nav-text" style="left:793px">Authors</div>
<div class="cart">$ 0.00<svg width="18" height="14" viewBox="0 0 18 14"><path d="M1 1h3l2 8h9l2-6H5" fill="none" stroke="#fff" stroke-width="1.4"/><circle cx="7" cy="12" r="1.4" fill="#fff"/><circle cx="14" cy="12" r="1.4" fill="#fff"/></svg></div>

<div class="colour-band">
  <span class="swatch" style="left:180px;background:#cfcfcf"></span>
  <span class="swatch" style="left:203px;background:#8c8c8c"></span>
  <span class="swatch" style="left:226px;background:#f2a7bd"></span>
  <span class="swatch" style="left:249px;background:#9bb3dd"></span>
  <span class="swatch" style="left:272px;background:#8b5a2b"></span>
  <span class="swatch" style="left:295px;background:#7bc843"></span>
  <span class="swatch" style="left:318px;background:#2e3b6e"></span>
  <span class="swatch" style="left:341px;background:#2d6a1a"></span>
  <span class="swatch" style="left:364px;background:#d2282a"></span>
  <span class="swatch" style="left:387px;background:#5cc3c9"></span>
  <span class="swatch" style="left:410px;background:#e8562a"></span>
  <span class="swatch" style="left:433px;background:#f7a21b"></span>
  <span class="swatch" style="left:456px;background:#1e6fd9"></span>
  <span class="swatch" style="left:479px;background:#f6c32a"></span>
  <span class="swatch" style="left:502px;background:#e94a8f"></span>
  <span class="swatch" style="left:525px;background:#3a2f9a"></span>
  <span class="swatch" style="left:548px;background:#e0141a"></span>
  <span class="swatch" style="left:571px;background:#f7b731"></span>
  <span class="swatch" style="left:594px;background:#ee3e86"></span>
  <span class="swatch" style="left:617px;background:#1ea0e0"></span>
  <span class="swatch" style="left:640px;background:#4d9a1f"></span>
  <span class="swatch" style="left:663px;background:#1ad6e8"></span>
  <span class="swatch" style="left:686px;background:#f7893b"></span>
  <span class="swatch" style="left:709px;background:#8fe03a"></span>
  <span class="swatch" style="left:732px;background:#3b8be0"></span>
  <span class="swatch" style="left:755px;background:#111"></span>
  <span class="swatch" style="left:778px;background:#f6c400"></span>
  <span class="swatch" style="left:801px;background:#8b4513"></span>
</div>

<div class="hero" role="img" aria-label="Collage of colourful greeting cards with birthday and get well wishes"></div>
<div class="tags" style="top:156px">
  <span class="tag">All</span><span class="tag">Bears</span><span class="tag">Birthday</span><span class="tag">Cards</span><span class="tag">Cats</span><span class="tag">Congratulations!</span><span class="tag">Dogs</span><span class="tag">Flowers</span><span class="tag">Love</span>
</div>
<div class="tags" style="top:184px">
  <span class="tag">Children</span><span class="tag">Friends</span><span class="tag">Bears</span><span class="tag">Cats</span><span class="tag">Friends</span><span class="tag">Cards</span><span class="tag">Cats</span><span class="tag">Flowers</span><span class="tag">Cats</span>
</div>

<main class="board">
  <div class="col" style="left:9px">
    <article class="card"><div class="card-photo" role="img" aria-label="Product photo: black and white photo card standing before a fir garland" style="height:169px;background:linear-gradient(160deg,#3d5a2a,#8b8b7c 45%,#d8cdb6)"></div><div class="card-meta"><span>SCC-Quilt Card</span><span class="card-price">€ 1.79</span></div><div class="card-pin"><b>Pinned From</b>Lorem ipsum dolor sit amet, tetur adipiscing elit.</div></article>
    <article class="card"><div class="card-photo" role="img" aria-label="Product photo: geometric patterned card on a mesh stand" style="height:101px;background:linear-gradient(135deg,#4b5e2e,#c08a3e 50%,#d9b77a)"></div><div class="card-meta"><span>SCC-Quilt Card</span><span class="card-price">€ 1.79</span></div><div class="card-pin"><b>Pinned From</b>Lorem ipsum dolor sit amet, tetur adipiscing elit.</div></article>
    <article class="card"><div class="card-photo" role="img" aria-label="Product photo: stack of colourful illustrated cards with a sunflower card in front" style="height:168px;background:linear-gradient(150deg,#c9a780,#6a3fa8 40%,#e6a240 70%,#d7b58e)"></div><div class="card-meta"><span>SCC-Quilt Card</span><span class="card-price">€ 0.99</span></div><div class="card-pin"><b>Pinned From</b>Lorem ipsum dolor sit amet, tetur adipiscing elit.</div></article>
  </div>
  <div class="col" style="left:191px">
    <article class="card"><div class="card-photo" role="img" aria-label="Product photo: illustrated winter card on a wooden surface" style="height:100px;background:linear-gradient(160deg,#e7ddc8,#cdbfa5 60%,#5c5c5c)"></div><div class="card-meta"><span>SCC-Quilt Card</span><span class="card-price">€ 1.99</span></div><div class="card-pin"><b>Pinned From</b>Lorem ipsum dolor sit amet, tetur adipiscing elit.</div></article>
    <article class="card"><div class="card-photo" role="img" aria-label="Product photo: group of cream illustrated cards on a table" style="height:110px;background:linear-gradient(150deg,#6b5a48,#e3d3b8 45%,#8a8a84)"></div><div class="card-meta"><span>SCC-Quilt Card</span><span class="card-price">€ 0.99</span></div><div class="card-pin"><b>Pinned From</b>Lorem ipsum dolor sit amet, tetur adipiscing elit.</div></article>
    <article class="card"><div class="card-photo" role="img" aria-label="Product photo: cream card with a round cookie illustration" style="height:170px;background:linear-gradient(160deg,#e8d8bd,#d9c3a1 55%,#5a4a3c)"></div><div class="card-meta"><span>SCC-Quilt Card</span><span class="card-price">€ 1.79</span></div><div class="card-pin"><b>Pinned From</b>Lorem ipsum dolor sit amet, tetur adipiscing elit.</div></article>
  </div>
  <div class="col" style="left:373px">
    <article class="card"><div class="card-photo" role="img" aria-label="Product photo: card with a swirling green tree illustration" style="height:157px;background:radial-gradient(circle at 50% 40%,#7f8f5e,#c9b79c 60%,#e6d6c2)"></div><div class="card-meta"><span>SCC-Quilt Card</span><span class="card-price">€ 0.99</span></div><div class="card-pin"><b>Pinned From</b>Lorem ipsum dolor sit amet, tetur adipiscing elit.</div></article>
    <article class="card"><div class="card-photo" role="img" aria-label="Product photo: colourful illustrated cards fanned out" style="height:100px;background:linear-gradient(140deg,#3e3fa8,#e3a13a 45%,#c24a6a 75%,#d6b890)"></div><div class="card-meta"><span>SCC-Quilt Card</span><span class="card-price">€ 1.79</span></div><div class="card-pin"><b>Pinned From</b>Lorem ipsum dolor sit amet, tetur adipiscing elit.</div></article>
    <article class="card"><div class="card-photo" role="img" aria-label="Product photo: set of cream illustrated winter cards" style="height:146px;background:linear-gradient(150deg,#6a5a48,#ded0b6 45%,#8d8d88)"></div><div class="card-meta"><span>SCC-Quilt Card</span><span class="card-price">€ 1.79</span></div><div class="card-pin"><b>Pinned From</b>Lorem ipsum dolor sit amet, tetur adipiscing elit.</div></article>
  </div>
</main>

<svg class="spinner" width="34" height="34" viewBox="0 0 34 34" aria-label="Loading">
  <g stroke-width="2.2" stroke-linecap="round">
    <line x1="17" y1="3" x2="17" y2="10" stroke="#333"/>
    <line x1="27" y1="7" x2="22" y2="12" stroke="#444"/>
    <line x1="31" y1="17" x2="24" y2="17" stroke="#555"/>
    <line x1="27" y1="27" x2="22" y2="22" stroke="#777"/>
    <line x1="17" y1="31" x2="17" y2="24" stroke="#888"/>
    <line x1="7" y1="27" x2="12" y2="22" stroke="#999"/>
    <line x1="3" y1="17" x2="10" y2="17" stroke="#aaa"/>
    <line x1="7" y1="7" x2="12" y2="12" stroke="#bbb"/>
  </g>
</svg>

<footer class="footer">
  <div class="f-col" style="left:197px"><h4>CARDS</h4><ul><li>All Cards</li><li>Birthday Cards</li><li>Birth Card</li><li>New Baby Cards</li><li>Get Well Cards</li><li>Love/Valentine Cards</li><li>Just beacues Cards</li></ul></div>
  <div class="f-col" style="left:350px"><h4>SPECIAL</h4><ul><li>Photo Cards</li><li>Magic Cards</li><li>Music Haves</li><li>Collections</li></ul></div>
  <div class="f-col" style="left:485px"><h4>MORE INFORMATION</h4><ul><li>How It Works</li><li>Pricing</li><li>Terms</li></ul></div>
  <div class="f-col" style="left:636px"><h4>ABOUT VELMORINO</h4><ul><li>Velmorino Corporate</li><li>Velmorino US</li><li>Velmorino EU</li><li>Velmorino DE</li><li>Velmorino NL</li></ul></div>
  <div class="f-col" style="left:784px"><h4>PAYMENT METHODS</h4><div class="pay"><span style="width:40px">Mercapay</span><span style="width:34px">Amtrel</span><span style="width:32px">Vistra</span><span style="width:52px">Paywell</span></div></div>
  <div class="copyright">Copyright © 2014 Velmorino<br>All Riights Reserved.</div>
</footer>
</body>
</html>
```